Sponsorship and registration document for Charity Golf Day 2022

The project requires 2 documents to be updated to look more graphically savvy and professionally presentable.
1. Charity golf day sponsorship document
2. One page registration document.
The text has been completed. Text not to be changed - just graphics.
New images would be preferred.
The logos have been provided.

Target Market(s)

Corporate Sponsors and Golf players

Requirements
Must have
• Golf Theme

```html
<!DOCTYPE html>
<html lang="en">
<head>
<meta charset="utf-8">
<title>Charity Golf Day – Sponsorship Proposal</title>
<link rel="stylesheet" href="https://fonts.googleapis.com/css2?family=Montserrat:wght@300;400;500;600;700;800;900&display=swap">
<style>
  :root {
    --stage: #3f3f42;
    --paper: #ffffff;
    --navy: #17468f;
    --blue: #1f5499;
    --lime: #d5df2b;
    --lime-pale: #f6f8d6;
    --mist: #eceef0;
    --grey-text: #6b6c70;
    --ink: #1d1d1f;
    --turf-a: #3f8f2c;
    --turf-b: #6fb33e;
  }
  * { margin: 0; padding: 0; box-sizing: border-box; }
  html, body { width: 1200px; height: 606px; overflow: hidden; background: var(--stage); }
  body { font-family: 'Montserrat', sans-serif; position: relative; }

  .page {
    position: absolute; top: 60px; width: 343px; height: 486px;
    background: var(--paper); overflow: hidden;
    box-shadow: 0 4px 10px rgba(0,0,0,.35);
  }
  .page--cover { left: 64px; }
  .page--contents { left: 428px; }
  .page--letter { left: 792px; }
  .page-art { position: absolute; inset: 0; }
  .abs { position: absolute; }

  /* cover */
  .cover-title { left: 22px; top: 24px; color: var(--navy); font-weight: 900; line-height: .9; }
  .cover-title .line-1 { font-size: 35px; display: block; letter-spacing: -.5px; }
  .cover-title .line-2 { font-size: 47px; display: block; letter-spacing: -1px; margin-top: 2px; }
  .cover-date { left: 22px; top: 124px; color: var(--grey-text); font-weight: 600; font-size: 21px; line-height: 21px; }
  .cover-venue { left: 20px; top: 170px; color: var(--grey-text); font-weight: 300; font-size: 37px; line-height: 35px; }
  .cover-url { left: 70px; width: 250px; top: 311px; text-align: center; color: var(--navy); font-weight: 600; font-size: 8.5px; }
  .cover-band { left: 0; width: 343px; top: 333px; text-align: center; color: #fff; font-weight: 900; font-size: 28px; line-height: 29px; }
  .cover-tagline { left: 60px; width: 240px; top: 401px; text-align: center; color: var(--navy); font-weight: 600; font-size: 8px; }
  .cover-pitch { left: 28px; top: 432px; width: 150px; color: var(--navy); font-weight: 700; font-size: 7.4px; line-height: 9px; }

  .club-mark { display: flex; align-items: center; gap: 5px; color: var(--navy); font-weight: 500; }
  .club-mark .mark-name { text-align: right; line-height: 1.05; }
  .club-mark .mark-dot { border-radius: 50%; background: var(--lime); flex: none; }
  .cover-mark { right: 18px; top: 428px; font-size: 17px; }
  .cover-mark .mark-dot { width: 36px; height: 36px; }
  .head-mark { right: 12px; top: 15px; font-size: 12px; }
  .head-mark .mark-dot { width: 24px; height: 24px; }

  /* inner header */
  .doc-header { left: 15px; top: 21px; font-weight: 800; font-size: 8.4px; line-height: 10.5px; color: #fff; }
  .doc-header .sub { color: var(--lime); font-style: italic; display: block; }

  /* contents */
  .contents-title { left: 34px; top: 110px; color: var(--navy); font-weight: 900; font-size: 17px; }
  .contents-list { left: 34px; top: 142px; width: 273px; list-style: none; }
  .contents-list li { display: flex; justify-content: space-between; font-weight: 700; font-size: 9.7px; height: 20.8px; color: var(--ink); }
  .contact { left: 34px; top: 326px; font-size: 7px; line-height: 8.4px; color: var(--ink); font-weight: 500; }
  .contact h3 { font-size: 11px; font-weight: 600; line-height: 12px; }
  .contact .second { margin-top: 17px; }

  /* letter */
  .letter { left: 23px; top: 73px; width: 298px; color: var(--ink); font-size: 6.8px; line-height: 8.4px; font-weight: 500; }
  .letter .lead { color: var(--navy); font-weight: 800; font-size: 8.6px; line-height: 10.4px; margin-bottom: 18px; }
  .letter p { margin-bottom: 8px; }
  .letter .gap { margin-bottom: 20px; }
  .format-list { list-style: none; margin: 7px 0 20px; }
  .format-list li { display: flex; align-items: center; gap: 4px; }
  .format-list svg { width: 7px; height: 7px; flex: none; }
  .sign-off { margin-top: 22px; margin-bottom: 20px; }
</style>
</head>
<body>

<!-- Cover -->
<section class="page page--cover">
  <svg class="page-art" viewBox="0 0 343 486" aria-hidden="true">
    <polygon points="262,0 343,0 343,150 318,160" fill="#a9aaad"/>
    <polygon points="135,0 190,0 262,105 225,110" fill="var(--lime)"/>
    <polygon points="180,0 192,0 250,108 240,110" fill="#fff"/>
    <polygon points="0,430 70,486 30,486 0,462" fill="var(--mist)"/>
    <polygon points="0,405 100,486 80,486 0,420" fill="var(--mist)"/>
    <circle cx="252" cy="215" r="114" fill="var(--lime)"/>
    <defs>
      <radialGradient id="turf" cx=".5" cy=".45" r=".6">
        <stop offset="0" stop-color="var(--turf-b)"/>
        <stop offset="1" stop-color="var(--turf-a)"/>
      </radialGradient>
    </defs>
    <circle cx="252" cy="215" r="106" fill="url(#turf)" role="img" aria-label="Photo of golf clubs in a white bag with golf balls and a tee on green turf"/>
    <polygon points="90,327 343,327 343,308 110,308" fill="var(--lime)"/>
    <rect x="0" y="327" width="343" height="70" fill="var(--blue)"/>
    <polygon points="170,327 343,327 343,397 250,397" fill="var(--navy)" opacity=".5"/>
    <polygon points="50,397 343,397 343,410 310,417 70,417" fill="var(--lime)"/>
  </svg>

  <h1 class="abs cover-title"><span class="line-1">CHARITY</span><span class="line-2">GOLF DAY</span></h1>
  <p class="abs cover-date">Friday 25<br>March 2022</p>
  <p class="abs cover-venue">Elm<br>Golf<br>Club</p>
  <p class="abs cover-url">www.fcev.org.au/golf-day</p>
  <h2 class="abs cover-band">SPONSORSHIP<br>PROPOSAL</h2>
  <p class="abs cover-tagline">Supporting Prostate Cancer Research</p>
  <p class="abs cover-pitch">Help us hit prostate cancer off the green and beat the most common cancer in Australian men.</p>
  <div class="abs club-mark cover-mark"><span class="mark-name">Eastvale<br>Fairway</span><span class="mark-dot"></span></div>
</section>

<!-- Contents -->
<section class="page page--contents">
  <svg class="page-art" viewBox="0 0 343 486" aria-hidden="true">
    <polygon points="150,0 230,0 343,260 343,430" fill="var(--lime-pale)"/>
    <polygon points="250,0 290,0 343,120 343,210" fill="var(--lime-pale)"/>
    <polygon points="200,0 343,0 343,60 250,60" fill="var(--mist)" opacity=".6"/>
    <polygon points="0,0 154,0 168,45 0,45" fill="var(--navy)"/>
  </svg>
  <p class="abs doc-header">CHARITY GOLF DAY<span class="sub">SPONSORSHIP PROPOSAL</span></p>
  <div class="abs club-mark head-mark"><span class="mark-name">Eastvale<br>Fairway</span><span class="mark-dot"></span></div>

  <h2 class="abs contents-title">CONTENTS:</h2>
  <ol class="abs contents-list">
    <li><span>Charity Golf Day Invitation</span><span>2</span></li>
    <li><span>About Prostate Cancer</span><span>3</span></li>
    <li><span>Why are we asking you to be involved</span><span>3</span></li>
    <li><span>What to expect</span><span>4</span></li>
    <li><span>Sponsorship Opportunities</span><span>5</span></li>
    <li><span>Application Form</span><span>7</span></li>
  </ol>

  <div class="abs contact">
    <h3>Contact :</h3>
    <p>Mara (Kostas) Bennett<br>Convenor<br>Co - President, Fairway Club of Eastvale<br>Mobile: 0400 555 210<br>Email: marabennett@mailbox.com<br>Web: www.fcev.org.au/golf-day</p>
    <p class="second">Livia Marchetti<br>Event Manager<br>Email: livia.marchetti@netmail.com</p>
  </div>
</section>

<!-- Letter -->
<section class="page page--letter">
  <svg class="page-art" viewBox="0 0 343 486" aria-hidden="true">
    <polygon points="150,0 230,0 343,260 343,430" fill="var(--lime-pale)"/>
    <polygon points="250,0 290,0 343,120 343,210" fill="var(--lime-pale)"/>
    <polygon points="200,0 343,0 343,60 250,60" fill="var(--mist)" opacity=".6"/>
    <polygon points="0,0 154,0 168,45 0,45" fill="var(--navy)"/>
  </svg>
  <p class="abs doc-header">CHARITY GOLF DAY<span class="sub">SPONSORSHIP PROPOSAL</span></p>
  <div class="abs club-mark head-mark"><span class="mark-name">Eastvale<br>Fairway</span><span class="mark-dot"></span></div>

  <div class="abs letter">
    <p class="lead">Join us for an exclusive day on the private Elm Golf Course, with all proceeds going to support Prostate Cancer Research, Awareness and Support.</p>
    <p>The Fairway Club of Eastvale will again be holding its Charity Golf Day with all proceeds used to support the Prostate Cancer Research, awareness and Support Programs. The venue will be the prestigious Elm Golf Club on Friday 25 March 2022, with a shotgun start at 8:00 am.</p>
    <p class="gap">We have enclosed for your information a copy of our promotional sponsor packages that outline the event, sponsorship package options and inclusions.</p>
    <p style="margin-bottom:0">The format of the day involves:</p>
    <ul class="format-list">
      <li><svg viewBox="0 0 10 10"><circle cx="5" cy="5" r="4" fill="none" stroke="var(--ink)" stroke-width="1"/><path d="M3 5l1.6 1.6L9 1.5" fill="none" stroke="var(--ink)" stroke-width="1.2"/></svg>Player registration, refreshments and light breakfast from 7:00am</li>
      <li><svg viewBox="0 0 10 10"><circle cx="5" cy="5" r="4" fill="none" stroke="var(--ink)" stroke-width="1"/><path d="M3 5l1.6 1.6L9 1.5" fill="none" stroke="var(--ink)" stroke-width="1.2"/></svg>Ambrose competition starting at 8:00am</li>
      <li><svg viewBox="0 0 10 10"><circle cx="5" cy="5" r="4" fill="none" stroke="var(--ink)" stroke-width="1"/><path d="M3 5l1.6 1.6L9 1.5" fill="none" stroke="var(--ink)" stroke-width="1.2"/></svg>Two Course lunch and presentations in the club house from 12:30pm</li>
    </ul>
    <p>Your commitment to supporting health programs in our community is truly appreciated. With assistance from sponsors such as yourself, we will continue to see improvements in the support and treatment for men and their families with prostate cancer.</p>
    <p>We hope that you will consider supporting the worthwhile event that is open to any organisation or individual who wishes to enjoy the benefits of playing golf at the prestigious Elm Golf Club.</p>
    <p>For more information, please check the website ( www.fcev.org.au/golf-day) or should you wish to discuss any aspect of the event, please contact me on 0400 555 210.</p>
    <p class="sign-off">Yours sincerely</p>
    <p>Mara (Kostas) Bennett<br>Convener<br>Co - President 2021 -2022<br>Secretary 2021 - 2022<br>Fairway Club of Eastvale</p>
  </div>
</section>

</body>
</html>
```